2 page brouchure for a Property Valuation company.

We require a 2 page brochure (printed front and back) for a property valuation company known as 'Brookmere Valuations'.

Brookmere valuations provides independent, reliable, accurate valuation services to our clients on the value of their properties to enable confidence and certainty in their decision.

The brochure is to be used to convey that the company provides valuation services for 8 main purposes and across 4 different property types.

The 8 main purposes for valuation include:
- Pre-Purchase Valuations
- Stamp Duty Valuations
-Capital Gains Tax (CGT)Valuations
-Unit Entitlement Valuations
-Family Law and Litigation Valuations
-Easement Valuations
-Wills & Probate Valuations
-Insolvency/Asset Realisation Valuations

The 4 main property types are:
-Residential
-Commercial
-Industrial
-Retail.

The brochure should have a title page, a page for the services, a page for the property types and a rear page with contact details.
Contact detail will include;
email:
phone :
Post :
website:

The words 'property valuation and advisory services' should be used at the front of the brochure.

The brochure should be professional and is used to convey information using visual aid and is to be used for promotion.

Our main colors are dark green and grey as seen in our logo.

We have attached our logo to add to the brochure and visit our website at: www.brookmerevaluations-example.com.au for more information about the company.

Please let me know if there are any further questions.

Target Market(s)

Solicitors/Lawyers
Accountants
Surveyors
Builders/Developers

Requirements
Must have
• Logo Colors, Logo, 8 Main services, 4 main property types, contact details.
Nice to have
• Should have concise visual aids to convey message.

Please add that we provide fast 48 hour turnaround for short form valuations. Maybe use a visual aid to convey this.

```html
<!DOCTYPE html>
<html lang="en">
<head>
<meta charset="utf-8">
<title>Brookmere Valuations – Brochure</title>
<link href="https://fonts.googleapis.com/css2?family=Roboto:wght@400;500;700&family=Raleway:wght@500&display=swap" rel="stylesheet">
<style>
  :root{
    --green:#1d7442;
    --green-dark:#166236;
    --green-deep:#12552e;
    --white:#ffffff;
    --ink:#3a3a3a;
    --grey-bg:#eeeeee;
    --rule:rgba(255,255,255,.55);
  }
  *{box-sizing:border-box;margin:0;padding:0}
  html,body{width:1200px;height:1000px;overflow:hidden;background:var(--grey-bg);font-family:"Roboto",Arial,sans-serif}
  .canvas{position:relative;width:1200px;height:1000px}
  .sheets{position:absolute;left:270px;top:18px;width:612px;transform:scale(1.08);transform-origin:0 0}
  .spread{position:relative;width:612px;height:432px;display:flex;box-shadow:0 4px 10px rgba(0,0,0,.18)}
  .spread + .spread{margin-top:30px}
  .page{position:relative;width:306px;height:432px;overflow:hidden}

  /* back cover */
  .back-cover{background:var(--green)}
  .back-cover .brand{position:absolute;top:344px;left:0;right:0;display:flex;justify-content:center;align-items:center;gap:6px;color:var(--white)}
  .brand-square{width:14px;height:14px;background:var(--white)}
  .brand-name{font-family:"Raleway",sans-serif;font-weight:500;font-size:9px;letter-spacing:1.6px;line-height:1.1;text-transform:uppercase}
  .back-cover .rule{position:absolute;top:372px;left:40px;right:40px;height:1px;background:var(--rule)}
  .contact-title{position:absolute;top:379px;left:0;right:0;text-align:center;color:var(--white);font-weight:700;font-size:7px}
  .contact-list{position:absolute;top:392px;left:78px;right:30px;display:flex;flex-wrap:wrap;gap:6px 16px;color:var(--white);font-size:5.6px}
  .contact-list span{display:flex;align-items:center;gap:3px}
  .contact-list svg{width:6px;height:6px;fill:var(--white)}

  /* front cover */
  .front-cover{background:var(--white)}
  .front-cover .brand{position:absolute;top:26px;left:44px;display:flex;align-items:center;gap:12px}
  .front-cover .brand-square{width:44px;height:44px;background:var(--green)}
  .front-cover .brand-name{color:#333;font-size:19px;letter-spacing:3.6px;line-height:1.05}
  .cover-bar{position:absolute;top:95px;left:84px;width:153px;height:10px;background:var(--green)}
  .cover-photo{position:absolute;top:102px;left:0;width:306px;height:228px;
    background:linear-gradient(180deg,#5b94c9 0%,#a9c8e2 30%,#8d9aa2 48%,#6f7a6c 65%,#4b5a3c 100%)}
  .cover-band{position:absolute;top:330px;left:0;right:0;bottom:0;background:linear-gradient(180deg,var(--green) 0%,var(--green-dark) 100%)}
  .cover-title{position:absolute;top:24px;left:0;right:0;text-align:center;color:var(--white);font-size:15.5px;font-weight:400;line-height:20px}
  .cover-web{position:absolute;bottom:16px;left:0;right:0;text-align:center;color:rgba(255,255,255,.85);font-size:6.5px}

  /* about page */
  .about{background:var(--white)}
  .page-heading{position:absolute;left:22px;top:22px;color:var(--green);font-size:12px;font-weight:700}
  .about-copy{position:absolute;top:60px;left:22px;right:22px;color:var(--ink);font-size:6.6px;line-height:9.2px;text-align:justify}
  .about-copy p{margin-bottom:7px}
  .guarantee{position:absolute;top:238px;left:0;right:0;bottom:0;background:var(--green)}
  .guarantee-title{position:absolute;top:14px;left:22px;right:22px;display:flex;align-items:center;gap:10px;color:var(--white);font-size:11px;font-weight:700}
  .guarantee-title::before,.guarantee-title::after{content:"";flex:1;height:1px;background:var(--rule)}
  .promise-grid{position:absolute;top:46px;left:14px;right:14px;display:grid;grid-template-columns:repeat(3,1fr);row-gap:16px}
  .promise{text-align:center;color:var(--white);font-size:6.3px;line-height:8px}
  .promise-icon{display:block;margin:0 auto 6px;width:28px;height:28px;fill:var(--white)}
  .promise-icon.line-icon{fill:none;stroke:var(--white)}

  /* types page */
  .types{background:var(--white)}
  .types .page-heading{left:27px}
  .tile-grid{position:absolute;top:62px;left:27px;width:255px;display:grid;grid-template-columns:120px 120px;gap:20px 15px}
  .tile{position:relative;height:73px;border-radius:0 10px 0 10px;overflow:hidden}
  .tile-photo{position:absolute;inset:0}
  .tile-residential .tile-photo{background:linear-gradient(135deg,#c9c3bc,#8f8479 60%,#5a5e68)}
  .tile-industrial .tile-photo{background:linear-gradient(180deg,#5f87b8,#9db2c4 55%,#6f7780)}
  .tile-commercial .tile-photo{background:linear-gradient(180deg,#a9c7e6,#6f97c2 60%,#8ca1b3)}
  .tile-retail .tile-photo{background:linear-gradient(180deg,#d3a545,#a7702a 55%,#6b4722)}
  .tile-label{position:absolute;left:0;right:0;bottom:0;height:12px;background:var(--green);border-radius:0 0 0 10px;color:var(--white);font-size:6px;font-weight:700;text-align:center;line-height:12px;text-transform:uppercase;letter-spacing:.2px}
  .types .services-title{position:absolute;top:248px;left:28px;color:var(--green);font-size:11.5px;font-weight:700}
  .service-list{position:absolute;top:288px;left:28px;width:250px;display:grid;grid-template-columns:1fr 1fr;grid-auto-flow:column;grid-template-rows:repeat(4,auto);gap:6px 8px;list-style:none;color:var(--ink);font-size:6.4px;line-height:8px}
  .service-list li{display:flex;gap:6px}
  .service-list li::before{content:"✓";color:var(--green);font-weight:700}
  .quote-band{position:absolute;left:0;right:0;bottom:0;height:66px;background:linear-gradient(180deg,var(--green) 0%,var(--green-deep) 100%);color:var(--white);text-align:center;padding-top:20px}
  .quote-band strong{display:block;font-size:11px;font-weight:700}
  .quote-band span{display:block;font-size:10px;margin-top:2px}
</style>
</head>
<body>
<main class="canvas">
  <div class="sheets">

    <section class="spread outer">
      <article class="page back-cover">
        <div class="brand"><span class="brand-square"></span><span class="brand-name">Brookmere<br>Valuations</span></div>
        <div class="rule"></div>
        <p class="contact-title">Need A Quote? Contact Us Now!</p>
        <div class="contact-list">
          <span><svg viewBox="0 0 10 10"><path d="M2 1l2 2-1 1.5c.6 1.2 1.4 2 2.5 2.5L7 6l2 2-1.5 1.5C4 9 1 6 .5 2.5z"/></svg>1300 555 014</span>
          <span><svg viewBox="0 0 10 10"><circle cx="5" cy="5" r="5"/></svg>info@brookmerevaluations-example.com.au</span>
          <span><svg viewBox="0 0 10 10"><path d="M5 0a3.5 3.5 0 0 1 3.5 3.5C8.5 6 5 10 5 10S1.5 6 1.5 3.5A3.5 3.5 0 0 1 5 0z"/></svg>PO Box 512 Sampleton NSW 2000</span>
        </div>
      </article>

      <article class="page front-cover">
        <div class="brand"><span class="brand-square"></span><span class="brand-name">Brookmere<br>Valuations</span></div>
        <div class="cover-photo" role="img" aria-label="Photo of a city skyline and harbour bridge above terrace-house rooftops under a blue cloudy sky"></div>
        <div class="cover-bar"></div>
        <div class="cover-band">
          <h1 class="cover-title">Property Valuation and<br>Advisory Services</h1>
          <p class="cover-web">www.brookmerevaluations-example.com.au</p>
        </div>
      </article>
    </section>

    <section class="spread inner">
      <article class="page about">
        <h2 class="page-heading">About BMV</h2>
        <div class="about-copy">
          <p>Brookmere Valuations emphasis is on providing the most accurate property valuations with transparency, and tailoring our services to meet our clients' individual needs.</p>
          <p>Our professional valuers are all members of the National Property Institute and carry an abundance of experience within the property valuation industry across a broad spectrum of property classes including residential, industrial, commercial and retail sectors.</p>
          <p>Our boutique valuation firm covers the Sydney metropolitan area and beyond including North Sydney and the eastern suburbs, inner city suburbs from Newtown to Strathfield, the greater western Sydney region from Parramatta, Blacktown to Penrith, the Canterbury-Bankstown region and south Sydney region from Hurstville to the Southern Shire.</p>
          <p>We are committed to providing the most accurate, reliable service to our clients which includes abiding by the National Property Institute's Code of Ethics and Practice Standards; realising continual growth and development by complying with, and drawing on, the latest industry legislation, standards, property intelligence and insights.</p>
        </div>
        <div class="guarantee">
          <h3 class="guarantee-title">Our Guarantee</h3>
          <div class="promise-grid">
            <div class="promise">
              <svg class="promise-icon" viewBox="0 0 28 28"><circle cx="17" cy="8" r="5"/><path d="M8 26c0-6 4-10 9-10s9 4 9 10z"/><circle cx="9" cy="10" r="4"/><path d="M1 25c0-5 3-8 8-8 1 0 2 .2 2.5.5C8.5 19 7 22 7 25z"/></svg>
              One on one interaction
            </div>
            <div class="promise">
              <svg class="promise-icon" viewBox="0 0 28 28"><text x="14" y="24" text-anchor="middle" font-family="Roboto, sans-serif" font-size="26" font-weight="700">$</text></svg>
              Free quote and initial<br>consultation
            </div>
            <div class="promise">
              <svg class="promise-icon line-icon" viewBox="0 0 28 28" stroke-width="1.6" stroke-linecap="round"><path d="M14 2a12 12 0 1 1-11 7" stroke-dasharray="3 2"/><path d="M14 7v7l5 3"/></svg>
              Reliable service<br>turnaround time
            </div>
            <div class="promise">
              <svg class="promise-icon" viewBox="0 0 28 28"><rect x="1" y="19" width="5" height="8"/><rect x="8" y="14" width="5" height="13"/><rect x="15" y="8" width="5" height="19"/><rect x="22" y="2" width="5" height="25"/></svg>
              Value adding to our<br>clients' long-term goals
            </div>
            <div class="promise">
              <svg class="promise-icon" viewBox="0 0 28 28"><path d="M14 1l3 2.5 4-.3 1 3.8 3.4 2-1.4 3.7 1.4 3.7-3.4 2-1 3.8-4-.3L14 27l-3-2.5-4 .3-1-3.8-3.4-2L4 15.3 2.6 11.6l3.4-2 1-3.8 4 .3z"/><path d="M9 14l3.5 3.5L19.5 10" style="fill:none;stroke:#1d7442;stroke-width:2.4"/></svg>
              Highly qualified valuers
            </div>
            <div class="promise">
              <svg class="promise-icon" viewBox="0 0 28 28"><path d="M1 8l5-2 3 9-4 2z"/><path d="M27 8l-5-2-3 9 4 2z"/><path d="M8 9l5-2 4 2 4-1 2 7-6 7-2-1-2 1-3-3-2-1z"/></svg>
              Building successful and<br>sustained relationships
            </div>
          </div>
        </div>
      </article>

      <article class="page types">
        <h2 class="page-heading">Property Types</h2>
        <div class="tile-grid">
          <div class="tile tile-residential"><div class="tile-photo" role="img" aria-label="Photo of a modern residential apartment building facade"></div><span class="tile-label">Residential Valuations</span></div>
          <div class="tile tile-industrial"><div class="tile-photo" role="img" aria-label="Photo of a large industrial warehouse interior"></div><span class="tile-label">Industrial Valuations</span></div>
          <div class="tile tile-commercial"><div class="tile-photo" role="img" aria-label="Photo of glass commercial office towers"></div><span class="tile-label">Commercial Valuations</span></div>
          <div class="tile tile-retail"><div class="tile-photo" role="img" aria-label="Photo of a golden-lit retail shopping arcade"></div><span class="tile-label">Retail Valuations</span></div>
        </div>
        <h2 class="services-title">Valuation Services</h2>
        <ul class="service-list">
          <li>Pre-Purchase Valuations</li>
          <li>Stamp Duty Valuations</li>
          <li>Capital Gains Tax Valuations</li>
          <li>Unit Entitlement Valuations</li>
          <li>Family Law &amp; Litigation Valuations</li>
          <li>Easement Valuations</li>
          <li>Wills &amp; Probate Valuations</li>
          <li>Insolvency/Asset<br>Realisation Valuations</li>
        </ul>
        <div class="quote-band">
          <strong>REQUEST FOR A QUOTE</strong>
          <span>Call Us Now! 1300 555 014</span>
        </div>
      </article>
    </section>

  </div>
</main>
</body>
</html>
```